Dean harlowe realestate

We want something complete different to our website now and something that will stand out this is our website http://deanharlowerealestate-demo.com/

our company website for my boss is www.stevenorrick-demo.com

please note this website is being made for dean harlowe not steven orrick

something similar to our company website but has to be in the branding of dean harlowe realestate

```html
<!DOCTYPE html>
<html lang="en">
<head>
<meta charset="utf-8">
<title>Dean Harlowe Property</title>
<link href="https://fonts.googleapis.com/css2?family=Roboto:wght@300;400;500;700;900&display=swap" rel="stylesheet">
<style>
:root{
  --orange:#f7750f;
  --dark:#1f2328;
  --text:#333;
  --muted:#777;
  --grey-bg:#f4f4f4;
  --line:#e6e6e6;
  --white:#fff;
  --night:#232a33;
}
*{box-sizing:border-box;margin:0;padding:0}
html,body{width:1200px;height:3364px;overflow:hidden}
body{position:relative;font-family:"Roboto",Arial,sans-serif;color:var(--text);background:var(--white)}
.abs{position:absolute}

/* hero */
.hero{left:0;top:0;width:1200px;height:597px;background:linear-gradient(180deg,#6f8aa8 0%,#a7b5c4 30%,#8c4a36 55%,#c8c2b8 75%,#4f5a3e 100%)}
.hero-shade{left:0;top:0;width:1200px;height:597px;background:linear-gradient(90deg,rgba(20,25,35,.55),rgba(20,25,35,.1) 60%,rgba(20,25,35,.2))}
.brand{left:132px;top:44px;color:var(--white);font-size:22px;font-weight:500;display:flex;align-items:center;gap:10px}
.brand-mark{width:14px;height:14px;background:var(--orange)}
.nav{left:474px;top:50px;display:flex;gap:0}
.nav a{position:absolute;color:var(--white);font-size:11px;font-weight:700;text-decoration:none;white-space:nowrap;letter-spacing:.3px}
.nav a.active::after{content:"";position:absolute;left:50%;margin-left:-9px;top:18px;width:18px;height:3px;background:var(--orange)}
.call-btn{left:895px;top:39px;width:173px;height:37px;border-radius:19px;background:var(--orange);color:var(--white);font-size:14px;font-weight:700;display:flex;align-items:center;justify-content:center}
.hero-kicker{left:146px;top:206px;color:var(--white);font-size:13px;font-weight:700}
.hero-title{left:144px;top:234px;color:var(--white);font-size:30px;font-weight:900;line-height:38px}
.hero-btn{left:146px;top:322px;width:120px;height:30px;border-radius:15px;background:var(--white);color:var(--orange);font-size:10px;font-weight:700;display:flex;align-items:center;justify-content:center}
.appraisal{left:675px;top:185px;width:393px;height:277px;background:var(--white)}
.appraisal-tab{left:0;top:0;height:34px;padding:0 40px 0 18px;background:var(--orange);color:var(--white);font-size:13px;font-weight:700;display:flex;align-items:center;clip-path:polygon(0 0,92% 0,100% 50%,92% 100%,0 100%)}
.field{position:absolute;background:#ececec;color:#aaa;font-size:9px;padding:10px 10px}
.submit{position:absolute;left:199px;top:215px;width:173px;height:40px;background:var(--orange);color:var(--white);font-size:11px;font-weight:700;display:flex;align-items:center;justify-content:center}

/* latest */
.latest-bg{left:0;top:597px;width:1200px;height:1033px;background:var(--grey-bg);clip-path:polygon(0 0,100% 0,100% 86%,0 100%)}
.sec-kicker{width:1200px;left:0;text-align:center;color:var(--orange);font-size:12px;font-weight:700}
.sec-title{width:1200px;left:0;text-align:center;color:var(--dark);font-size:24px;font-weight:500}
.sec-sub{width:1200px;left:0;text-align:center;color:var(--muted);font-size:11px}
.card{position:absolute;width:291px;height:356px;background:var(--white);box-shadow:0 2px 6px rgba(0,0,0,.06)}
.card-photo{width:291px;height:173px}
.badge{position:absolute;left:0;top:0;height:20px;padding:0 20px 0 8px;background:var(--orange);color:var(--white);font-size:10px;font-weight:700;display:flex;align-items:center;clip-path:polygon(0 0,85% 0,100% 50%,85% 100%,0 100%)}
.view-label{position:absolute;left:0;top:78px;width:291px;text-align:center;color:var(--white);font-size:11px}
.card-body{padding:14px 18px}
.card-title{font-size:13px;font-weight:700;color:var(--dark)}
.card-desc{margin-top:9px;font-size:10.5px;line-height:17px;color:var(--muted);height:34px}
.specs{margin-top:12px;display:flex;gap:20px;font-size:10px;color:#555;align-items:center}
.specs span{display:flex;align-items:center;gap:8px}
.status{margin-top:12px;font-size:9.5px;color:var(--orange)}
.price{margin-top:4px;font-size:17px;font-weight:700;color:var(--orange);letter-spacing:.5px}

/* featured */
.slide-photo{left:277px;top:1750px;width:655px;height:331px;background:linear-gradient(180deg,#8fb4d6 0%,#c9d8e4 35%,#c9a983 60%,#6b7a4c 100%)}
.slide-card{left:347px;top:1942px;width:492px;height:231px;background:var(--white);box-shadow:0 2px 8px rgba(0,0,0,.08)}
.slide-card .card-body{padding:30px 36px}
.arrow{width:44px;height:44px;border-radius:50%;border:1px solid #ddd;background:var(--white);display:flex;align-items:center;justify-content:center}

/* testimonial */
.testi-bg{left:0;top:2175px;width:1200px;height:480px;background:linear-gradient(180deg,#3a4452,#1c222b);clip-path:polygon(0 22%,100% 0,100% 83%,0 100%)}
.quote-mark{color:var(--orange);font-size:110px;font-weight:900;line-height:1;font-family:Georgia,serif}
.testi-head{width:1200px;left:0;text-align:center;color:var(--white);font-size:13px;font-weight:700}
.testi-sub{width:1200px;left:0;text-align:center;color:#aab;font-size:10px}
.avatar{left:481px;top:2356px;width:88px;height:79px;background:linear-gradient(180deg,#c9b9a8,#8d7a6a)}
.testi-name{left:587px;top:2368px;color:var(--white);font-size:11px;font-weight:700}
.testi-role{left:587px;top:2392px;color:#ddd;font-size:10px}
.testi-text{left:270px;top:2455px;width:660px;text-align:center;color:#e6e6e6;font-size:12px;line-height:21px}
.dots{left:0;width:1200px;top:2544px;display:flex;justify-content:center;gap:8px}
.dots i{width:7px;height:7px;border-radius:50%;background:#bbb;display:block}
.dots i.on{background:transparent;border:1px solid #fff}

/* agent */
.agent-photo{left:173px;top:2728px;width:239px;height:305px;background:linear-gradient(180deg,#dcdcdc 0%,#c99a80 35%,#2a3240 65%,#1c222b 100%);clip-path:polygon(0 0,100% 0,100% 88%,0 100%)}
.about-title{left:502px;top:2682px;font-size:14px;font-weight:700;color:var(--dark)}
.about-title em{font-style:normal;color:var(--orange)}
.about-title::after{content:"";position:absolute;left:0;top:24px;width:44px;height:2px;background:var(--orange)}
.agent-name{left:502px;top:2728px;font-size:11px;font-weight:700;color:var(--dark)}
.agent-role{left:502px;top:2750px;font-size:10px;color:var(--muted)}
.agent-bio{left:502px;top:2776px;width:570px;font-size:10.5px;line-height:22px;color:var(--muted)}
.info-label{font-size:11px;font-weight:700;color:var(--dark)}
.info-val{margin-top:6px;font-size:10.5px;color:var(--muted)}

/* footer */
.footer-bg{left:0;top:3040px;width:1200px;height:324px;background:linear-gradient(180deg,#2a3038,#14181d);clip-path:polygon(0 0,100% 25%,100% 100%,0 100%)}
.foot-col{position:absolute;top:3192px;display:flex;gap:16px}
.foot-label{color:var(--white);font-size:11px;font-weight:700}
.foot-val{margin-top:8px;color:#ddd;font-size:12px;line-height:22px}
.socials{margin-top:10px;display:flex;gap:8px}
.socials span{width:22px;height:22px;background:#2a8fd6;display:block}
.socials span.red{background:#d9302c}
.socials span.blue{background:#3b5998}
.socials span.teal{background:#1f7fb6}
.foot-rule{left:132px;top:3298px;width:936px;height:1px;background:rgba(255,255,255,.12)}
.copyright{left:0;width:1200px;top:3318px;text-align:center;color:#aaa;font-size:10px}
</style>
</head>
<body>

<!-- hero -->
<div class="abs hero" role="img" aria-label="Photo of a two-storey house with a red tiled roof under a cloudy sky"></div>
<div class="abs hero-shade"></div>
<div class="abs brand"><span class="brand-mark"></span>Dean Harlowe Property</div>
<nav class="abs nav">
  <a class="active" style="left:0">HOME</a>
  <a style="left:60px">FOR SALE</a>
  <a style="left:139px">AGENTS</a>
  <a style="left:210px">BOOK APPRAISAL</a>
  <a style="left:331px">CONTACT US</a>
</nav>
<div class="abs call-btn">Call us : 0400 123 487</div>
<div class="abs hero-kicker">WANNA A FINA A DREAM HOME..!</div>
<div class="abs hero-title">DEAN HARLOWE PROPERTY<br>Always with you</div>
<div class="abs hero-btn">VIEW MORE</div>

<form class="abs appraisal">
  <div class="abs appraisal-tab">BOOK AN APPRAISAL</div>
  <div class="field" style="left:20px;top:56px;width:173px;height:38px">Full Name</div>
  <div class="field" style="left:199px;top:56px;width:173px;height:38px">Email Address</div>
  <div class="field" style="left:20px;top:103px;width:173px;height:38px">Phone Number</div>
  <div class="field" style="left:199px;top:103px;width:173px;height:38px">Address</div>
  <div class="field" style="left:20px;top:150px;width:173px;height:105px">Message</div>
  <div class="field" style="left:199px;top:150px;width:173px;height:38px">Preferred Time / Day</div>
  <div class="submit">BOOK NOW</div>
</form>

<!-- latest properties -->
<div class="abs latest-bg"></div>
<div class="abs sec-kicker" style="top:619px">Latest</div>
<div class="abs sec-title" style="top:640px">Properties</div>
<div class="abs sec-sub" style="top:676px">Check out some of our recent properties.</div>

<svg width="0" height="0" style="position:absolute">
  <defs>
    <symbol id="i-bed" viewBox="0 0 20 14"><path d="M1 2v11M1 9h18v4M3 9V6h6v3M10 9V5h8v4" fill="none" stroke="#555" stroke-width="1.4"/></symbol>
    <symbol id="i-bath" viewBox="0 0 20 14"><path d="M1 6h18M2 6c0 5 3 7 8 7s8-2 8-7M4 6V2h3" fill="none" stroke="#555" stroke-width="1.4"/></symbol>
    <symbol id="i-area" viewBox="0 0 16 16"><path d="M2 1h9l3 3v11H2z M11 1v3h3" fill="none" stroke="#555" stroke-width="1.4"/></symbol>
  </defs>
</svg>

<article class="card" style="left:132px;top:733px">
  <div class="card-photo" role="img" aria-label="Photo of a white house with a red roof and garden" style="background:linear-gradient(180deg,#9cc0e0,#d8d2c4 50%,#5e7a3c)"></div>
  <div class="badge">Featured</div>
  <div class="card-body">
    <div class="card-title">Home in Merrick Way</div>
    <div class="card-desc">Enchanting three bedroom, three bath home with spacious one bedroom,...</div>
    <div class="specs"><span><svg width="20" height="14"><use href="#i-bed"/></svg>3</span><span><svg width="20" height="14"><use href="#i-bath"/></svg>3</span><span><svg width="16" height="16"><use href="#i-area"/></svg>4300 Sq Ft</span></div>
    <div class="status">For Sale</div>
    <div class="price">$540,000</div>
  </div>
</article>

<article class="card" style="left:453px;top:733px">
  <div class="card-photo" role="img" aria-label="Photo of a beige villa with a garage" style="background:linear-gradient(180deg,#6f9ccc,#c4bba4 55%,#6d7f4a)"></div>
  <div class="badge">Featured</div>
  <div class="view-label">View Property</div>
  <div class="card-body">
    <div class="card-title">Villa in Coral Gables</div>
    <div class="card-desc">Enjoy serenity of Deering Bay whole day from this spectacular...</div>
    <div class="specs"><span><svg width="20" height="14"><use href="#i-bed"/></svg>3</span><span><svg width="20" height="14"><use href="#i-bath"/></svg>3</span><span><svg width="16" height="16"><use href="#i-area"/></svg>4300 Sq Ft</span></div>
    <div class="status">For Sale</div>
    <div class="price">$825,000</div>
  </div>
</article>

<article class="card" style="left:777px;top:733px">
  <div class="card-photo" role="img" aria-label="Photo of a white villa with a red roof" style="background:linear-gradient(180deg,#9cc0e0,#d8d2c4 50%,#5e7a3c)"></div>
  <div class="card-body">
    <div class="card-title">Villa on Hollywood Boulevard</div>
    <div class="card-desc">The very best waterfront location in Harbor Islands complete with...</div>
    <div class="specs"><span><svg width="20" height="14"><use href="#i-bed"/></svg>3</span><span><svg width="20" height="14"><use href="#i-bath"/></svg>3</span><span><svg width="16" height="16"><use href="#i-area"/></svg>4300 Sq Ft</span></div>
    <div class="status">For Sale</div>
    <div class="price">$740,000</div>
  </div>
</article>

<article class="card" style="left:132px;top:1131px">
  <div class="card-photo" role="img" aria-label="Photo of a modern stone-clad restaurant building" style="background:linear-gradient(180deg,#e8ecef,#cfc6b8 60%,#8a8072)"></div>
  <div class="card-body">
    <div class="card-title">Traditional Food Restaurant</div>
    <div class="card-desc">We are an award winning and very unique concept inspired...</div>
    <div class="specs"><span><svg width="16" height="16"><use href="#i-area"/></svg>4300 Sq Ft</span></div>
    <div class="status">For Rent</div>
    <div class="price">$2,600 Monthly</div>
  </div>
</article>

<article class="card" style="left:453px;top:1131px">
  <div class="card-photo" role="img" aria-label="Photo of a modern villa with a swimming pool" style="background:linear-gradient(180deg,#7fb2dc,#d9d4c8 50%,#2fa4c9)"></div>
  <div class="badge">Featured</div>
  <div class="card-body">
    <div class="card-title">Villa in Coral Gables</div>
    <div class="card-desc">Enjoy serenity of Deering Bay whole day from this spectacular...</div>
    <div class="specs"><span><svg width="20" height="14"><use href="#i-bed"/></svg>3</span><span><svg width="20" height="14"><use href="#i-bath"/></svg>3</span><span><svg width="16" height="16"><use href="#i-area"/></svg>4300 Sq Ft</span></div>
    <div class="status">For Sale</div>
    <div class="price">$825,000</div>
  </div>
</article>

<article class="card" style="left:777px;top:1131px">
  <div class="card-photo" role="img" aria-label="Photo of a multi-storey office building" style="background:linear-gradient(180deg,#a8c4de,#9aa4ae 50%,#6d7680)"></div>
  <div class="card-body">
    <div class="card-title">Office Space at Northwest 107th</div>
    <div class="card-desc">The very best waterfront location in Harbor Islands complete with...</div>
    <div class="specs"><span><svg width="16" height="16"><use href="#i-area"/></svg>4300 Sq Ft</span></div>
    <div class="status">For Rent</div>
    <div class="price">$3,100 Monthly</div>
  </div>
</article>

<!-- featured -->
<div class="abs sec-kicker" style="top:1636px">Featured</div>
<div class="abs sec-title" style="top:1656px">Properties</div>
<div class="abs sec-sub" style="top:1693px">Check out our shortlisted properties</div>

<div class="abs arrow" style="left:170px;top:1888px"><svg width="10" height="12"><path d="M7 1 2 6l5 5" fill="none" stroke="#999" stroke-width="1.5"/></svg></div>
<div class="abs arrow" style="left:965px;top:1888px"><svg width="10" height="12"><path d="M3 1l5 5-5 5" fill="none" stroke="#999" stroke-width="1.5"/></svg></div>

<div class="abs slide-photo" role="img" aria-label="Photo of a large two-storey suburban house with trees"></div>
<article class="abs slide-card">
  <div class="badge" style="height:24px">Featured</div>
  <div class="card-body">
    <div class="card-title">Home in Merrick Way</div>
    <div class="card-desc" style="line-height:20px;height:40px">Enchanting three bedroom, three bath home with spacious one bedroom,<br>one bath cabana, in-laws quarters.</div>
    <div class="specs"><span><svg width="20" height="14"><use href="#i-bed"/></svg>3</span><span><svg width="20" height="14"><use href="#i-bath"/></svg>3</span><span><svg width="16" height="16"><use href="#i-area"/></svg>4300 Sq Ft</span></div>
    <div class="status">For Sale</div>
    <div class="price">$540,000</div>
  </div>
</article>

<!-- testimonial -->
<div class="abs testi-bg" role="img" aria-label="Dusk city skyline photo behind a dark overlay"></div>
<div class="abs quote-mark" style="left:164px;top:2236px">“</div>
<div class="abs quote-mark" style="left:958px;top:2532px">”</div>
<div class="abs testi-head" style="top:2283px">WHAT OUR CLIENTS THINK</div>
<div class="abs testi-sub" style="top:2305px">Check out what our client says about us</div>
<div class="abs avatar" role="img" aria-label="Portrait photo of the client"></div>
<div class="abs testi-name">Clara Wendell</div>
<div class="abs testi-role">Brand Manager</div>
<p class="abs testi-text">I found Dean to be different from most agents, in that he listened, and set a marketing program to suit the special features of our property. Eager to do anything to assist with a positive outcome, I'd recommend Dean for properties in the local area.</p>
<div class="abs dots"><i></i><i class="on"></i><i></i><i></i></div>

<!-- about agent -->
<div class="abs agent-photo" role="img" aria-label="Portrait photo of agent Dean Harlowe in a suit"></div>
<div class="abs about-title">ABOUT <em>AGENT</em></div>
<div class="abs agent-name">DEAN HARLOWE</div>
<div class="abs agent-role">Sales Partner</div>
<p class="abs agent-bio">Based in Perth from day one, Dean has approached his career in real estate with an ambition of building lasting relationships based on trust, confidence and integrity. Over a long period of time his experiences have consistently validated this attitude with Dean enjoying an abundance of referrals and repeat business throughout the Perth metropolitan market, from mid-high end residential property and residential land based developments.</p>

<div class="abs" style="left:502px;top:2890px;display:flex;gap:18px">
  <svg width="20" height="26" viewBox="0 0 20 26"><path d="M10 1a9 9 0 0 0-9 9c0 7 9 15 9 15s9-8 9-15a9 9 0 0 0-9-9z" fill="var(--orange)"/><circle cx="10" cy="10" r="3.5" fill="#fff"/></svg>
  <div><div class="info-label">ADDRESS</div><div class="info-val">Harbour View Road, Block-B, Eastport-2041</div></div>
</div>
<div class="abs" style="left:502px;top:2954px;display:flex;gap:18px">
  <svg width="20" height="22" viewBox="0 0 20 22"><path d="M4 2l4 5-2 3c1 3 3 5 6 6l3-2 4 4-3 3C8 21 0 12 1 5z" fill="var(--orange)"/></svg>
  <div><div class="info-label">PHONE</div><div class="info-val">(555) 201-0147, (555) 201-0188, (555) 301-0442</div></div>
</div>

<!-- footer -->
<div class="abs footer-bg" role="img" aria-label="Dark city skyline photo behind a dark overlay"></div>
<div class="foot-col" style="left:145px">
  <svg width="20" height="26" viewBox="0 0 20 26"><path d="M10 1a9 9 0 0 0-9 9c0 7 9 15 9 15s9-8 9-15a9 9 0 0 0-9-9z" fill="var(--orange)"/><circle cx="10" cy="10" r="3.5" fill="#1c2128"/></svg>
  <div><div class="foot-label">OFFICE ADDRESS</div><div class="foot-val">2710 Linden Ave, Willow Park,<br>Merrick Way, FL 10482</div></div>
</div>
<div class="foot-col" style="left:443px">
  <svg width="20" height="22" viewBox="0 0 20 22"><path d="M4 2l4 5-2 3c1 3 3 5 6 6l3-2 4 4-3 3C8 21 0 12 1 5z" fill="var(--orange)"/></svg>
  <div><div class="foot-label">PHONE NUMBER</div><div class="foot-val" style="font-size:14px">0400 123 487,<br>0400 123 592</div></div>
</div>
<div class="foot-col" style="left:793px">
  <svg width="22" height="22" viewBox="0 0 22 22"><circle cx="11" cy="11" r="9" fill="none" stroke="var(--orange)" stroke-width="2"/><path d="M2 11h18M11 2c-4 5-4 13 0 18M11 2c4 5 4 13 0 18" fill="none" stroke="var(--orange)" stroke-width="1.5"/></svg>
  <div><div class="foot-label">SOCIAL LINKS</div><div class="socials"><span></span><span class="red"></span><span class="blue"></span><span class="teal"></span></div></div>
</div>
<div class="abs foot-rule"></div>
<div class="abs copyright">© 2018. Dean Harlowe Property.com. All rights reserved.</div>

</body>
</html>
```